Fashion Label Startup Business Card Design

Maribel Quint is a startup fashion designer based on the Gold Coast in QLD Australia. Maribels label " Vorine by Quint " is based upon taking old world design techniques and infusing them modern twist. The card design should incorporate an old world theme using colours like mustard, ocha, black, white and elements of lace pattern.

Card Details:

Maribel Quint
Fashion Designer
P: 04 0152 6847
E: vorinebyquint@mailbrook.com
W: www.friendsnet.com/VOrineByQuint

```html
<!DOCTYPE html>
<html lang="en">
<head>
<meta charset="utf-8">
<title>Vorine by Quint — Business Card</title>
<link rel="stylesheet" href="https://fonts.googleapis.com/css2?family=Dancing+Script:wght@700&family=Open+Sans:ital,wght@0,300;0,400;1,300&display=swap">
<style>
  :root {
    --page: #ffffff;
    --taupe: #9c8b7c;
    --taupe-light: #aea295;
    --stripe: #b1a79d;
    --mocha: #7a6149;
    --lace: #c9bfb4;
    --ink-white: #ffffff;
    --ink-soft: #e6ded6;
  }
  * { margin: 0; padding: 0; box-sizing: border-box; }
  html, body {
    width: 1200px; height: 900px; overflow: hidden;
    background: var(--page);
    font-family: "Open Sans", Arial, sans-serif;
  }
  .card {
    position: absolute;
    background: var(--taupe);
    overflow: hidden;
    box-shadow: 1px 2px 4px rgba(0,0,0,0.35);
  }
  .card svg.decor { position: absolute; inset: 0; width: 100%; height: 100%; }
  .card--back { left: 46px; top: 210px; width: 537px; height: 346px; }
  .card--front { left: 615px; top: 325px; width: 543px; height: 352px; }

  .holder { position: absolute; left: 52px; top: 136px; }
  .holder__name {
    font-family: "Dancing Script", cursive;
    font-weight: 700; font-size: 38px; line-height: 1;
    color: var(--ink-white);
  }
  .holder__role {
    font-weight: 300; font-size: 17px; color: var(--ink-soft);
    margin-top: 2px;
  }
  .contact {
    position: absolute; left: 52px; top: 240px;
    list-style: none;
  }
  .contact li {
    display: flex; align-items: center; gap: 6px;
    height: 18px;
    font-style: italic; font-weight: 300; font-size: 14px;
    color: var(--ink-white);
  }
  .contact svg { width: 14px; height: 14px; flex: none; }

  .label {
    position: absolute; left: 0; right: 0; top: 150px;
    text-align: center;
    font-weight: 400; font-size: 44px; letter-spacing: 1px;
    color: var(--ink-white);
  }
</style>
</head>
<body>

<section class="card card--back">
  <svg class="decor" viewBox="0 0 537 346" preserveAspectRatio="none">
    <rect x="0" y="210" width="537" height="16" fill="var(--stripe)"/>
    <rect x="0" y="226" width="537" height="120" fill="var(--mocha)"/>
    <polygon role="img" aria-label="Diagonal band of cream lace pattern" points="0,18 135,0 414,0 0,80" fill="var(--lace)" opacity="0.55"/>
    <polygon role="img" aria-label="Diagonal band of cream lace pattern" points="160,346 537,272 537,322 400,346" fill="var(--lace)" opacity="0.6"/>
  </svg>
  <div class="holder">
    <p class="holder__name">Maribel Quint</p>
    <p class="holder__role">Fashion Designer</p>
  </div>
  <ul class="contact">
    <li>
      <svg viewBox="0 0 14 14"><circle cx="7" cy="7" r="6" fill="none" stroke="#fff" stroke-width="1.2"/><path d="M5 4 Q4 7 6.5 10 L8 9 L7 7.5 L6.5 8 Q5.6 6.5 6 5.2 L6.7 5 L6.3 3.5 Z" fill="#fff"/></svg>
      04 0152 6847
    </li>
    <li>
      <svg viewBox="0 0 14 14"><circle cx="7" cy="7" r="2.5" fill="none" stroke="#fff" stroke-width="1.3"/><path d="M9.5 7 V8.3 Q9.5 10 11 10 Q12.5 10 12.5 7 A5.5 5.5 0 1 0 9.5 11.8" fill="none" stroke="#fff" stroke-width="1.3"/></svg>
      vorinebyquint@mailbrook.com
    </li>
    <li>
      <svg viewBox="0 0 14 14"><circle cx="7" cy="7" r="6" fill="none" stroke="#fff" stroke-width="1.2"/></svg>
      www.friendsnet.com/VOrineByQuint
    </li>
  </ul>
</section>

<section class="card card--front">
  <svg class="decor" viewBox="0 0 543 352" preserveAspectRatio="none">
    <polygon role="img" aria-label="Diagonal band of cream lace pattern" points="105,0 543,0 543,82 330,20" fill="var(--lace)" opacity="0.55"/>
    <polygon role="img" aria-label="Diagonal band of cream lace pattern" points="0,274 385,352 0,352" fill="var(--lace)" opacity="0.55"/>
  </svg>
  <p class="label">Vorine by Quint</p>
</section>

</body>
</html>
```